Create a proposal + product powerpoint

Please see the powerpoint for the slides. There are about 20 slides to be created. Rest of them are for reference and show the design that I like.

I would like to move fast on this, since I need to present it next week (in the week of April 21st).

Please download the current content from here:
https://www.brindlecove.net/fetch/qTzWmRvBxLpYkNsHcD

Please make at least 4 slides with the specific content so I can assess your design style.

Target Market(s)

Business Audience and very senior technical audience
Decision Makers

Industry/Entity Type

Product

Colors
e34297
a64599

Requirements
Must have
• Should be very clean, crisp.

I like to use Icons as shown in the powerpoint.... Please see the appendix of the slide deck that shows the various icons. Most of them just have plain text, and I would like to organize so that it does not look like some is just reading text.

I would like to focus on the design aspects so that the audience is clear on how the solution works.

Every page should some graphic element based on the slides shown in the appendix.

```html
<!DOCTYPE html>
<html lang="en">
<head>
<meta charset="utf-8">
<title>Sandbox policies are inadequate</title>
<link rel="stylesheet" href="https://fonts.googleapis.com/css2?family=Sarabun:wght@400;500&display=swap">
<style>
  :root {
    --title-purple: #9c1596;
    --icon-dark: #5e1f5f;
    --icon-light: #8a3a88;
    --footer-left: #a01a5c;
    --footer-left-end: #9a1c6c;
    --footer-right: #a64599;
    --rule-grey: #d6d6d6;
    --logo-grey: #9a9a9a;
    --ink: #111111;
    --white: #ffffff;
    --facet-light: #f3d9f2;
    --facet-mid: #e2a3e2;
    --facet-deep: #c765d3;
  }
  html, body {
    margin: 0;
    padding: 0;
    overflow: hidden;
  }
  .slide {
    position: relative;
    width: 1200px;
    height: 900px;
    overflow: hidden;
    background:
      radial-gradient(ellipse 260px 200px at 40px 640px, rgba(198, 120, 200, 0.28), transparent 70%),
      radial-gradient(ellipse 300px 160px at 60px 260px, rgba(220, 170, 220, 0.18), transparent 70%),
      var(--white);
    font-family: "Sarabun", sans-serif;
    color: var(--ink);
  }
  .facet-backdrop {
    position: absolute;
    top: 92px;
    right: 0;
    width: 300px;
    height: 742px;
    background:
      linear-gradient(90deg, rgba(255,255,255,1) 0%, rgba(255,255,255,0) 35%),
      linear-gradient(160deg, var(--facet-deep) 0%, var(--facet-mid) 30%, var(--facet-light) 60%, var(--facet-mid) 85%, var(--facet-light) 100%);
  }
  .slide-header {
    position: absolute;
    top: 0;
    left: 0;
    right: 0;
    height: 91px;
    border-bottom: 2px solid var(--rule-grey);
    background: var(--white);
  }
  .slide-title {
    position: absolute;
    left: 40px;
    top: 14px;
    margin: 0;
    font-size: 49px;
    font-weight: 400;
    color: var(--title-purple);
    letter-spacing: 0.3px;
  }
  .logo-placeholder {
    position: absolute;
    top: 9px;
    right: 15px;
    width: 148px;
    height: 70px;
    box-sizing: border-box;
    border: 2px solid #e6e6e6;
    border-radius: 8px;
    display: flex;
    align-items: center;
    justify-content: center;
    font-size: 28px;
    color: var(--logo-grey);
    letter-spacing: 1px;
  }
  .point-list {
    position: absolute;
    left: 54px;
    top: 186px;
    margin: 0;
    padding: 0;
    list-style: none;
  }
  .point {
    display: flex;
    align-items: center;
    height: 143px;
    margin-bottom: 52px;
  }
  .point-icon {
    width: 146px;
    height: 143px;
    border-radius: 6px;
    background: radial-gradient(circle at 50% 50%, var(--icon-light) 0%, var(--icon-dark) 100%);
    box-shadow: 0 3px 8px rgba(90, 20, 90, 0.25);
    display: flex;
    align-items: center;
    justify-content: center;
    flex-shrink: 0;
  }
  .icon-dollar {
    font-size: 118px;
    line-height: 1;
    color: var(--white);
    font-weight: 400;
  }
  .icon-artwork {
    width: 106px;
    height: 106px;
    border-radius: 50%;
  }
  .icon-artwork.stopwatch {
    background: radial-gradient(circle, #ffffff 0%, #e4e4e4 55%, #9a9a9a 100%);
  }
  .icon-artwork.puzzle {
    width: 110px;
    height: 84px;
    border-radius: 4px;
    background: linear-gradient(180deg, #ffffff 0%, #e8e0e8 100%);
  }
  .point-text {
    margin-left: 44px;
    font-size: 38px;
    font-weight: 400;
    letter-spacing: 0.4px;
  }
  .slide-footer {
    position: absolute;
    left: 0;
    bottom: 0;
    width: 1200px;
    height: 58px;
  }
  .footer-band {
    position: absolute;
    inset: 0;
  }
  .footer-page,
  .footer-copyright {
    position: absolute;
    top: 12px;
    font-size: 24px;
    color: var(--white);
    font-weight: 500;
  }
  .footer-page { left: 14px; }
  .footer-copyright { right: 14px; }
</style>
</head>
<body>
<main class="slide">
  <div class="facet-backdrop" role="img" aria-label="Decorative faceted triangle pattern in soft pink and purple"></div>

  <header class="slide-header">
    <h1 class="slide-title">Sandbox policies are inadequate.</h1>
    <div class="logo-placeholder">LOGO HERE</div>
  </header>

  <ul class="point-list">
    <li class="point">
      <div class="point-icon"><span class="icon-dollar">$</span></div>
      <span class="point-text">Sandboxes are expensive</span>
    </li>
    <li class="point">
      <div class="point-icon">
        <div class="icon-artwork stopwatch" role="img" aria-label="Stopwatch icon"></div>
      </div>
      <span class="point-text">Refresh cycles are long</span>
    </li>
    <li class="point">
      <div class="point-icon">
        <div class="icon-artwork puzzle" role="img" aria-label="Puzzle pieces icon with one piece missing"></div>
      </div>
      <span class="point-text">Sandbox policies are inadequate.</span>
    </li>
  </ul>

  <footer class="slide-footer">
    <svg class="footer-band" width="1200" height="58" viewBox="0 0 1200 58" aria-hidden="true">
      <defs>
        <linearGradient id="footerLeftFill" x1="0" x2="1" y1="0" y2="0">
          <stop offset="0" stop-color="var(--footer-left)"/>
          <stop offset="1" stop-color="var(--footer-left-end)"/>
        </linearGradient>
      </defs>
      <polygon points="0,0 906,0 940,58 0,58" fill="url(#footerLeftFill)"/>
      <polygon points="918,6 1200,6 1200,58 952,58" fill="var(--footer-right)"/>
    </svg>
    <span class="footer-page">Page : 01</span>
    <span class="footer-copyright">Copyright text here</span>
  </footer>
</main>
</body>
</html>
```